Auto Repair Specialist needs wordpress design

We are looking for a Word Press website design for a Brisk Truck Service and Repair Specialist shop called Kelvarro. The design should have a slightly retro Industrial feel. You can see our logo and an example of our sign in attached files.

Coded - Design and coding required

```html
<!DOCTYPE html>
<html lang="en">
<head>
<meta charset="utf-8">
<title>Kelvarro – Brisk Truck Repair and Service</title>
<link rel="stylesheet" href="https://fonts.googleapis.com/css2?family=League+Spartan:wght@500;600;700&family=Poppins:wght@400;500;600&family=Lato:ital,wght@1,400&display=swap">
<style>
:root{
  --navy:#29388f;
  --ink:#2e2e2e;
  --heading-gray:#4f4f4f;
  --gold:#f2a81d;
  --white:#fff;
}
*{box-sizing:border-box;margin:0;padding:0}
html,body{width:1200px;height:4110px;overflow:hidden;background:var(--white)}
body{position:relative;font-family:"Poppins",sans-serif;color:var(--ink)}
.abs{position:absolute}
.heading{font-family:"League Spartan",sans-serif;font-weight:600;color:var(--heading-gray)}
.heading b{color:var(--navy);font-weight:600}
.photo{position:absolute}

.topbar{left:0;top:0;width:1200px;height:69px;background:var(--navy)}
.topbar .item{position:absolute;top:24px;display:flex;align-items:center;gap:8px;color:var(--white);font-size:13px}
.topbar svg{fill:var(--white)}

.navbar{left:0;top:69px;width:1200px;height:73px;background:var(--white);border-bottom:3px solid #8d8d8d}
.brand{position:absolute;display:flex;align-items:center;gap:8px;font-weight:600;color:var(--navy)}
.brand .dot{width:18px;height:18px;border-radius:50%;background:var(--navy)}
.nav-link{position:absolute;top:24px;font-size:12.5px;font-weight:500;color:#333}
.nav-link.active{color:var(--navy);font-weight:600}
.nav-sep{position:absolute;top:12px;width:2px;height:40px;background:#7d7d7d}
.btn{position:absolute;display:flex;align-items:center;justify-content:center;background:var(--navy);color:var(--white);font-weight:600;font-size:13px;border-radius:3px}
.link-more{position:absolute;color:var(--navy);font-weight:600;font-size:13px}

.hero-title{left:690px;top:356px;font-size:46px;color:#5a5a5a}
.hero-sub{left:704px;top:428px;font-size:20px;color:#4a4a4a}

.section-title{font-size:38px}
.body-copy{font-size:13.5px;line-height:20px;text-align:justify;color:#333}

.card-photo{border:3px solid var(--navy);border-radius:24px 0 24px 0}
.card-title{font-weight:600;font-size:17px;color:#222}
.card-copy{font-size:13.5px;line-height:20px;color:#555}
.card-icon svg{stroke:var(--navy);fill:none;stroke-width:2}

.why-bg{left:0;top:2099px;width:1200px;height:534px;background:linear-gradient(160deg,#fdfdfd 0%,#ececec 40%,#f7f7f7 60%,#e5e5e5 100%)}
.why-item{position:absolute;left:163px;display:flex;align-items:center;gap:12px;font-size:13.5px;color:#666}
.why-item svg{stroke:var(--navy);fill:none;stroke-width:1.6}

.quote{position:absolute;width:232px;font-family:"Lato",sans-serif;font-style:italic;font-size:12px;line-height:19px;color:#666;text-align:center}
.stars{position:absolute;color:var(--gold);font-size:16px;letter-spacing:2px}
.person{position:absolute;font-family:"Lato",sans-serif;font-style:italic;font-size:12.5px;color:#333}
.person small{font-size:9.5px;color:#888}
.quote-mark{position:absolute;font-family:"League Spartan",sans-serif;font-weight:700;font-size:64px;color:var(--navy);line-height:1}

.cta{left:0;top:3272px;width:1200px;height:383px;background:var(--navy);overflow:hidden}
.cta-title{font-family:"League Spartan",sans-serif;font-weight:600;font-size:37px;line-height:43px;color:var(--white);text-align:center}
.cta-copy{color:var(--white);font-size:13.5px;line-height:20px;text-align:center}

.foot-head{position:absolute;font-size:16px;font-weight:500;color:var(--navy)}
.foot-link{position:absolute;display:flex;align-items:center;gap:8px;font-size:13px;color:#333}
.foot-link svg{fill:var(--navy)}
.social{position:absolute;width:30px;height:30px;border-radius:50%;background:var(--navy)}
.copyright{left:0;top:3996px;width:1200px;text-align:center;font-size:13px;color:#333}
</style>
</head>
<body>

<div class="abs topbar">
  <div class="item" style="left:282px">
    <svg width="12" height="15" viewBox="0 0 12 16"><path d="M6 0a6 6 0 0 0-6 6c0 4.5 6 10 6 10s6-5.5 6-10a6 6 0 0 0-6-6zm0 8.5A2.5 2.5 0 1 1 6 3.5a2.5 2.5 0 0 1 0 5z"/></svg>
    Specializing In Brisk Truck Repair And Service
  </div>
  <div class="item" style="left:619px">
    <svg width="20" height="14" viewBox="0 0 20 14"><path d="M0 0h20v14H0z M1.5 1.5 10 8l8.5-6.5" fill="#fff" stroke="#29388f" stroke-width="1.4"/></svg>
    <span style="margin-left:4px">Mail Us :sales@kelvarroautos.com</span>
  </div>
  <div class="item" style="left:902px">
    <svg width="18" height="18" viewBox="0 0 24 24"><path d="M6.6 10.8a15.1 15.1 0 0 0 6.6 6.6l2.2-2.2a1 1 0 0 1 1-.25 11.4 11.4 0 0 0 3.6.57 1 1 0 0 1 1 1V20a1 1 0 0 1-1 1A17 17 0 0 1 3 4a1 1 0 0 1 1-1h3.5a1 1 0 0 1 1 1c0 1.25.2 2.45.57 3.6a1 1 0 0 1-.25 1z"/></svg>
    <span style="margin-left:6px">Call Us : (555) 014-2815</span>
  </div>
</div>

<div class="abs navbar">
  <div class="brand" style="left:30px;top:22px;font-size:20px"><span class="dot"></span>Kelvarro, LLC</div>
  <span class="nav-link active" style="left:260px">Home</span>
  <span class="nav-sep" style="left:343px"></span>
  <span class="nav-link" style="left:394px">About Us</span>
  <span class="nav-sep" style="left:498px"></span>
  <span class="nav-link" style="left:549px">Our Services</span>
  <span class="nav-sep" style="left:670px"></span>
  <span class="nav-link" style="left:722px">Testimonies</span>
  <span class="nav-sep" style="left:840px"></span>
  <span class="nav-link" style="left:891px">Portfolio</span>
  <span class="btn" style="left:1005px;top:12px;width:125px;height:37px">CONTACT US ›</span>
</div>

<!-- hero -->
<div class="photo" role="img" aria-label="Blue heavy-duty pickup truck before a city skyline, framed by a sweeping blue curve" style="left:0;top:145px;width:1200px;height:590px;background:linear-gradient(90deg,#dfe2ee 0%,#eceaf2 45%,#f6f5f9 70%,#ffffff 100%)"></div>
<div class="abs heading hero-title">Welcome To Kelvarro</div>
<div class="abs hero-sub">Specializing In Brisk Truck Repair And Service</div>
<span class="btn" style="left:862px;top:479px;width:120px;height:29px;font-size:11px;font-weight:500">EXPLORE MORE</span>

<!-- about -->
<div class="abs heading section-title" style="left:180px;top:845px">About Us</div>
<p class="abs body-copy" style="left:180px;top:900px;width:392px">Lorem ipsum dolor sit amet, consectetur adipiscing elit, sed do eiusmod tempor incididunt ut labore et dolore magna aliqua. Vulputate dignissim suspendisse in est ante. Faucibus turpis in eu mi bibendum neque. Sodales ut etiam sit amet nisl purus. Velit laoreet id donec ultrices tincidunt.</p>
<span class="btn" style="left:181px;top:1049px;width:123px;height:35px;font-size:12.5px">KNOW MORE ›</span>
<div class="photo" role="img" aria-label="Blue sedan framed by a gear shape" style="left:606px;top:806px;width:428px;height:372px;background:linear-gradient(180deg,#f3f4f9 0%,#e4e7f2 100%)"></div>

<!-- services -->
<div class="abs heading section-title" style="left:0;top:1325px;width:1200px;text-align:center">Our <b>Services</b></div>

<div class="photo card-photo" role="img" aria-label="Mechanic changing a truck wheel" style="left:86px;top:1420px;width:305px;height:383px;background:linear-gradient(180deg,#4a5068 0%,#6b645c 100%)"></div>
<div class="photo card-photo" role="img" aria-label="Blue car being washed" style="left:447px;top:1420px;width:305px;height:383px;background:linear-gradient(180deg,#2d6f98 0%,#4f8fae 100%)"></div>
<div class="photo card-photo" role="img" aria-label="Couple choosing a car in a showroom" style="left:808px;top:1420px;width:305px;height:383px;background:linear-gradient(180deg,#c9c8c8 0%,#6b6f7a 100%)"></div>

<div class="abs card-title" style="left:140px;top:1825px">Repair</div>
<div class="abs card-title" style="left:501px;top:1825px">Service</div>
<div class="abs card-title" style="left:862px;top:1825px">Sale</div>

<div class="abs card-icon" style="left:86px;top:1860px"><svg width="40" height="36" viewBox="0 0 40 36"><circle cx="14" cy="9" r="6"/><path d="M3 34c0-8 5-13 11-13s11 5 11 13"/><path d="M28 4l8 8-14 14"/></svg></div>
<div class="abs card-icon" style="left:447px;top:1860px"><svg width="42" height="36" viewBox="0 0 42 36"><path d="M4 24l4-10h26l4 10v8H4z"/><circle cx="12" cy="28" r="3"/><circle cx="30" cy="28" r="3"/></svg></div>
<div class="abs card-icon" style="left:808px;top:1860px"><svg width="42" height="36" viewBox="0 0 42 36"><circle cx="10" cy="7" r="4"/><circle cx="28" cy="7" r="4"/><path d="M3 34V18c0-3 3-5 7-5s7 2 7 5v16M21 34V18c0-3 3-5 7-5s7 2 7 5v16"/></svg></div>

<p class="abs card-copy" style="left:140px;top:1860px;width:250px">Lorem ipsum dolor sit amet, consectetur adipiscing elit. Ut elit tellus, luctus nec ullamcorper mattis, pulvinar dapibus leo.</p>
<p class="abs card-copy" style="left:501px;top:1860px;width:250px">Lorem ipsum dolor sit amet, consectetur adipiscing elit. Ut elit tellus, luctus nec ullamcorper mattis, pulvinar dapibus leo.</p>
<p class="abs card-copy" style="left:862px;top:1860px;width:250px">Lorem ipsum dolor sit amet, consectetur adipiscing elit. Ut elit tellus, luctus nec ullamcorper mattis, pulvinar dapibus leo.</p>

<span class="link-more" style="left:190px;top:1964px">KNOW MORE ›</span>
<span class="link-more" style="left:551px;top:1964px">KNOW MORE ›</span>
<span class="link-more" style="left:912px;top:1964px">KNOW MORE ›</span>

<!-- why choose -->
<div class="abs why-bg"></div>
<div class="abs heading section-title" style="left:0;top:2120px;width:1200px;text-align:center">Why <b>Chose Us?</b></div>
<p class="abs body-copy" style="left:163px;top:2196px;width:340px">Lorem ipsum dolor sit amet, consectetur adipiscing elit, sed do eiusmod tempor incididunt ut labore et dolore magna aliqua. Vulputate dignissim suspendisse in est ante. Faucibus turpis in eu mi bibendum neque. Sodales ut etiam sit amet nisl purus. Velit laoreet id donec ultrices tincidunt.</p>

<div class="why-item" style="top:2343px"><svg width="26" height="26" viewBox="0 0 26 26"><circle cx="13" cy="8" r="5"/><path d="M3 25c0-6 4-10 10-10s10 4 10 10z"/></svg>Professional staff</div>
<div class="why-item" style="top:2390px"><svg width="26" height="26" viewBox="0 0 26 26"><path d="M3 3l20 20M23 3L3 23M3 3h5v5M23 23h-5v-5"/></svg>Quality Services</div>
<div class="why-item" style="top:2437px"><svg width="26" height="26" viewBox="0 0 26 26"><path d="M13 2l9 4v7c0 6-4 10-9 11-5-1-9-5-9-11V6z"/></svg>Long Term Warranty</div>
<div class="why-item" style="top:2484px"><svg width="26" height="26" viewBox="0 0 26 26"><path d="M3 12h5v12H3zM8 13l5-10c2 0 3 2 2 5l-1 3h8c2 0 3 2 2 4l-3 8c-1 1-2 2-3 2H8"/></svg>100% Customer Satisfaction</div>
<div class="why-item" style="top:2531px"><svg width="26" height="26" viewBox="0 0 26 26"><path d="M13 2l2 4 4 .5-3 3 1 4-4-2-4 2 1-4-3-3 4-.5z"/><circle cx="6" cy="19" r="2.5"/><circle cx="20" cy="19" r="2.5"/></svg>High rated reviews from customers</div>

<div class="photo" role="img" aria-label="Orange pickup truck" style="left:510px;top:2290px;width:631px;height:325px;background:linear-gradient(180deg,#d98a3a 0%,#b86416 100%);border-radius:6px"></div>

<!-- testimonials -->
<div class="abs heading section-title" style="left:0;top:2706px;width:1200px;text-align:center">What Our <b>Clients Say?</b></div>

<div class="photo" role="img" aria-label="Portrait of client Marcus" style="left:247px;top:2798px;width:115px;height:118px;background:#d9d8d8"></div>
<div class="photo" role="img" aria-label="Portrait of client Rita" style="left:541px;top:2798px;width:115px;height:118px;background:#d2cfcd"></div>
<div class="photo" role="img" aria-label="Portrait of client Albert" style="left:839px;top:2798px;width:115px;height:118px;background:#d3d6dc"></div>

<div class="quote-mark" style="left:385px;top:2808px">”</div>
<div class="quote-mark" style="left:681px;top:2808px">”</div>
<div class="quote-mark" style="left:978px;top:2808px">”</div>

<p class="quote" style="left:187px;top:2928px">“Nisl nunc mi ipsum faucibus vitae aliquet. Non sodales neque sodales ut etiam sit amet nisl purus. Adipiscing at in tellus integer feugiat scelerisque. Dignissim enim sit amet venenatis urna cursus eget. Volutpat est velit egestas dui id. Viverra justo nec ultrices dui sapien eget mi proin. Eget sit amet tellus cras. Ultrices sagittis orci a scelerisque purus semper.”</p>
<p class="quote" style="left:482px;top:2928px">“Nisl nunc mi ipsum faucibus vitae aliquet. Non sodales neque sodales ut etiam sit amet nisl purus. Adipiscing at in tellus integer feugiat scelerisque. Dignissim enim sit amet venenatis urna cursus eget. Volutpat est velit egestas dui id. Viverra justo nec ultrices dui sapien eget mi proin. Eget sit amet tellus cras. Ultrices sagittis orci a scelerisque purus semper.”</p>
<p class="quote" style="left:781px;top:2928px">“Nisl nunc mi ipsum faucibus vitae aliquet. Non sodales neque sodales ut etiam sit amet nisl purus. Adipiscing at in tellus integer feugiat scelerisque. Dignissim enim sit amet venenatis urna cursus eget. Volutpat est velit egestas dui id. Viverra justo nec ultrices dui sapien eget mi proin. Eget sit amet tellus cras. Ultrices sagittis orci a scelerisque purus semper.”</p>

<div class="stars" style="left:258px;top:3126px">★★★★★</div>
<div class="stars" style="left:553px;top:3126px">★★★★★</div>
<div class="stars" style="left:852px;top:3126px">★★★★★</div>

<div class="person" style="left:248px;top:3148px">Marcus Dell <small>CORVANE CEO</small></div>
<div class="person" style="left:544px;top:3148px">Rita Vance <small>CORVANE CEO</small></div>
<div class="person" style="left:836px;top:3148px">Albert Quill <small>CORVANE CEO</small></div>

<!-- call to action -->
<div class="abs cta">
  <div class="photo" role="img" aria-label="Blue pickup truck, front three-quarter view, with white diagonal stripes" style="left:560px;top:0;width:640px;height:383px;background:linear-gradient(90deg,#2b3b92 0%,#34458f 100%)"></div>
  <div class="abs cta-title" style="left:162px;top:38px;width:360px">Best Brisk Truck<br>Repair Services</div>
  <div class="abs" style="left:178px;top:128px;width:328px;height:2px;background:#fff"></div>
  <p class="abs cta-copy" style="left:176px;top:162px;width:332px">Lorem ipsum dolor sit amet, consectetur adipiscing elit, sed do eiusmod tempor incididunt ut labore et dolore magna aliqua. Vulputate dignissim suspendisse in est ante. Faucibus turpis in eu mi bibendum neque. Sodales ut etiam sit amet nisl purus. Velit laoreet id donec ultrices tincidunt.</p>
  <span class="abs" style="left:290px;top:331px;color:#fff;font-weight:600;font-size:13px">CONTACT US ›</span>
</div>

<!-- footer -->
<div class="brand" style="left:116px;top:3775px;font-size:20px"><span class="dot"></span>Kelvarro, LLC</div>
<p class="abs" style="left:70px;top:3840px;width:230px;text-align:center;font-size:13px;line-height:19px;color:#333">Specializing In Brisk Truck Repair And Service</p>
<span class="social" style="left:134px;top:3906px"></span>
<span class="social" style="left:170px;top:3906px"></span>
<span class="social" style="left:206px;top:3906px"></span>

<div class="foot-head" style="left:407px;top:3742px">Our Company</div>
<div class="foot-link" style="left:420px;top:3777px"><svg width="15" height="13" viewBox="0 0 16 14"><path d="M8 0l8 7h-2v7h-4V9H6v5H2V7H0z"/></svg>Home</div>
<div class="foot-link" style="left:420px;top:3809px"><svg width="17" height="13" viewBox="0 0 18 14"><circle cx="9" cy="4" r="3"/><circle cx="3.5" cy="5" r="2"/><circle cx="14.5" cy="5" r="2"/><path d="M3 14c0-4 3-6 6-6s6 2 6 6z"/></svg>About Us</div>
<div class="foot-link" style="left:420px;top:3841px"><svg width="15" height="14" viewBox="0 0 16 16"><path d="M16 0C10 1 6 4 4 9l3 3c5-2 8-6 9-12zM3 10l-3 2 2 2-2 2 4-1 1-2z"/></svg>Testimonies</div>
<div class="foot-link" style="left:420px;top:3873px"><svg width="17" height="13" viewBox="0 0 18 14"><path d="M2 7l2-5h10l2 5h2v5h-2a2.5 2.5 0 0 1-5 0H7a2.5 2.5 0 0 1-5 0H0V7z"/></svg>Portfolio</div>

<div class="foot-head" style="left:690px;top:3742px">Our Services</div>
<div class="foot-link" style="left:697px;top:3777px"><svg width="14" height="14" viewBox="0 0 16 16"><path d="M0 2l2-2 14 14-2 2zM16 2l-2-2-5 5 2 2zM0 14l2 2 5-5-2-2z"/></svg>Repair</div>
<div class="foot-link" style="left:697px;top:3809px"><svg width="17" height="13" viewBox="0 0 18 14"><circle cx="6" cy="4" r="3"/><path d="M0 14c0-4 3-6 6-6s6 2 6 6z"/><circle cx="14" cy="9" r="3.5"/></svg>Service</div>
<div class="foot-link" style="left:697px;top:3841px"><svg width="16" height="14" viewBox="0 0 18 16"><path d="M0 0h3l1 3h14l-3 7H5L2 2H0z"/><circle cx="6" cy="14" r="1.8"/><circle cx="14" cy="14" r="1.8"/></svg>Sale</div>

<div class="foot-head" style="left:967px;top:3742px">Get In Touch</div>
<div class="foot-link" style="left:893px;top:3777px;align-items:flex-start"><svg width="12" height="15" viewBox="0 0 12 16" style="margin-top:6px"><path d="M6 0a6 6 0 0 0-6 6c0 4.5 6 10 6 10s6-5.5 6-10a6 6 0 0 0-6-6zm0 8.5A2.5 2.5 0 1 1 6 3.5a2.5 2.5 0 0 1 0 5z"/></svg><span style="line-height:19px">Kelvarro, LLC 412 Millrace Ave<br>Harlow Bend, NC 27000</span></div>
<div class="foot-link" style="left:893px;top:3828px"><svg width="14" height="14" viewBox="0 0 24 24"><path d="M6.6 10.8a15.1 15.1 0 0 0 6.6 6.6l2.2-2.2a1 1 0 0 1 1-.25 11.4 11.4 0 0 0 3.6.57 1 1 0 0 1 1 1V20a1 1 0 0 1-1 1A17 17 0 0 1 3 4a1 1 0 0 1 1-1h3.5a1 1 0 0 1 1 1c0 1.25.2 2.45.57 3.6a1 1 0 0 1-.25 1z"/></svg>(555) 014-2815</div>
<div class="foot-link" style="left:893px;top:3860px;gap:4px"><svg width="20" height="14" viewBox="0 0 20 14"><path d="M0 0h20v14H0z"/><path d="M1.5 1.5 10 8l8.5-6.5" fill="none" stroke="#fff" stroke-width="1.4"/></svg>sales@kelvarroautos.com</div>

<div class="abs copyright">Copyright © 2022 KelvarroTrucks | Powered by KelvarroTrucks</div>

</body>
</html>
```